Brightstone Roofing Business Card

This is my current business card. But I’d like to make some changes. Somewhere on the card I’d like to list some of the services we offer. Maybe on the back? But I’d still like to keep the red. White and black modern look.

-residential & commercial roofing
-Roof Repairs & Maintenance
-Storm Damage & Insurance Claims specialist
-Christmas Lights and permanent Christmas lights
Fencing. Windows. Gutters. Siding. Sheetrock, painting.

```html
<!DOCTYPE html>
<html lang="en">
<head>
<meta charset="UTF-8">
<title>Brightstone Roofing Business Card</title>
<link href="https://fonts.googleapis.com/css2?family=Michroma&family=Work+Sans:wght@400;500&display=swap" rel="stylesheet">
<style>
  :root {
    --red: #e32028;
    --red-dark: #7a1115;
    --red-deep: #5a0c0f;
    --black: #141414;
    --ink: #222222;
    --paper: #f7f6f4;
    --backdrop: #d4d4d4;
  }
  * { margin: 0; padding: 0; box-sizing: border-box; }
  html, body { width: 1200px; height: 853px; overflow: hidden; }
  body {
    background: var(--backdrop);
    display: flex;
    align-items: center;
    justify-content: center;
    gap: 40px;
    font-family: "Work Sans", sans-serif;
  }
  .card {
    width: 520px;
    height: 297px;
    border-radius: 22px;
    overflow: hidden;
    position: relative;
    box-shadow: 0 6px 18px rgba(0,0,0,0.18);
  }

  /* Front */
  .card-front { background: var(--red-dark); }
  .tartan-fill {
    position: absolute; inset: 0;
    background: linear-gradient(135deg, var(--red) 0%, var(--red-dark) 45%, var(--red) 70%, var(--red-deep) 100%);
  }
  .front-brand {
    position: absolute; inset: 0;
    display: flex; flex-direction: column; align-items: center; justify-content: center;
    gap: 14px;
  }
  .brand-dot {
    width: 92px; height: 92px; border-radius: 50%;
    background: var(--red);
    border: 4px solid #ffffff;
  }
  .front-name {
    font-family: "Michroma", sans-serif;
    color: #ffffff;
    font-size: 24px;
    letter-spacing: 1px;
    text-align: center;
    line-height: 1.25;
  }

  /* Back */
  .card-back { background: var(--paper); }
  .back-brand {
    position: absolute; top: 26px; left: 0; right: 0;
    display: flex; flex-direction: column; align-items: center; gap: 8px;
  }
  .back-brand .brand-dot {
    width: 46px; height: 46px; border-width: 0;
  }
  .back-name {
    font-family: "Michroma", sans-serif;
    color: var(--red);
    font-size: 14px;
    text-align: center;
    line-height: 1.3;
  }
  .identity-row {
    position: absolute; top: 128px; left: 0; right: 0;
    display: flex; justify-content: center; align-items: center; gap: 22px;
  }
  .person { text-align: right; }
  .person-name {
    font-family: "Michroma", sans-serif;
    font-size: 17px; color: var(--black); letter-spacing: 1px;
  }
  .person-name .surname { color: var(--red); }
  .person-role { font-size: 12px; color: var(--red); letter-spacing: 1px; margin-top: 3px; }
  .divider { width: 1.5px; height: 58px; background: var(--ink); }
  .contact-list { list-style: none; font-size: 12.5px; color: var(--ink); }
  .contact-list li { display: flex; align-items: center; gap: 8px; line-height: 1.65; }
  .contact-list svg { width: 11px; height: 11px; fill: var(--red); flex: none; }
  .services {
    position: absolute; top: 206px; left: 24px; right: 24px;
    font-size: 8.6px; text-transform: uppercase; letter-spacing: 0.4px;
    color: var(--ink); text-align: center; line-height: 1.75;
  }
  .services .sep { color: var(--red); padding: 0 3px; }
  .stripe-band {
    position: absolute; left: 0; right: 0; bottom: 0; height: 14px;
    background: linear-gradient(90deg, var(--red-dark), var(--red), var(--red-dark));
  }
</style>
</head>
<body>
  <section class="card card-front">
    <div class="tartan-fill" role="img" aria-label="Red, black and white tartan plaid pattern"></div>
    <div class="front-brand">
      <div class="brand-dot"></div>
      <div class="front-name">BRIGHTSTONE<br>ROOFING CO.</div>
    </div>
  </section>

  <section class="card card-back">
    <div class="back-brand">
      <div class="brand-dot"></div>
      <div class="back-name">BRIGHTSTONE<br>ROOFING CO.</div>
    </div>

    <div class="identity-row">
      <div class="person">
        <div class="person-name">DEAN <span class="surname">CARVER</span></div>
        <div class="person-role">Owner</div>
      </div>
      <div class="divider"></div>
      <ul class="contact-list">
        <li>
          <svg viewBox="0 0 24 24" aria-hidden="true"><path d="M6.6 10.8a15.1 15.1 0 0 0 6.6 6.6l2.2-2.2a1 1 0 0 1 1-.25 11.4 11.4 0 0 0 3.6.57 1 1 0 0 1 1 1V20a1 1 0 0 1-1 1A17 17 0 0 1 3 4a1 1 0 0 1 1-1h3.5a1 1 0 0 1 1 1c0 1.25.2 2.45.57 3.57a1 1 0 0 1-.25 1z"/></svg>
          682-555-0148
        </li>
        <li>
          <svg viewBox="0 0 24 24" aria-hidden="true"><path d="M2 5h20v14H2z M2 5l10 8 10-8" /></svg>
          dean@brightstoneroofing.co
        </li>
        <li>
          <svg viewBox="0 0 24 24" aria-hidden="true"><path d="M12 2a10 10 0 1 0 0 20 10 10 0 0 0 0-20zm0 2c.9 1.2 1.6 2.8 1.9 4.5h-3.8C10.4 6.8 11.1 5.2 12 4zM4.3 13.5a8 8 0 0 1 0-3h3.4a17 17 0 0 0 0 3zm.8 2h3a12 12 0 0 0 1.6 4 8 8 0 0 1-4.6-4zm3-7h-3a8 8 0 0 1 4.6-4 12 12 0 0 0-1.6 4zM12 20c-.9-1.2-1.6-2.8-1.9-4.5h3.8c-.3 1.7-1 3.3-1.9 4.5zm2.2-6.5H9.8a15 15 0 0 1 0-3h4.4a15 15 0 0 1 0 3zm.1 6a12 12 0 0 0 1.6-4h3a8 8 0 0 1-4.6 4zm1.9-6a17 17 0 0 0 0-3h3.4a8 8 0 0 1 0 3zm-.3-5a12 12 0 0 0-1.6-4 8 8 0 0 1 4.6 4z"/></svg>
          www.brightstoneroofing.co
        </li>
      </ul>
    </div>

    <p class="services">
      Residential &amp; Commercial Roofing<span class="sep">|</span>Roof Repairs &amp; Maintenance<br>
      Storm Damage &amp; Insurance Claims Specialist<span class="sep">|</span>Christmas Lights and Permanent Christmas Lights<br>
      Fencing. Windows. Gutters. Siding. Sheetrock, Painting
    </p>

    <div class="stripe-band" role="img" aria-label="Red tartan plaid stripe border"></div>
  </section>
</body>
</html>
```